Willowmere Counseling (Endure - Mend - Flourish) - Double Sided Business Card

I would like a 2-sided business card. Front: Matte Black or Navy with Logo & Tagline. Back: Name, Address, Phone Number, Email, & Website (maybe would like to include a small map pin-pointing location); Prefer front to be a gold/silver foil (iridescent); Back prefer white or light colored background with lettering that is easy to read and simple

Target Market(s)

Individuals & Couples (13 y.o. - ALL Adults); High end clientele

Industry/Entity Type

Licensed Professional Counselor (Mental Health)

Contact Information for Business Card

Name: Willowmere Counseling; Tagline: Endure - Mend - Flourish; Address: 3870 N. Garrick Ave., Suite 214, Fort Worth, TX 76132; Phone: (214) 555-0187; Website: www.WillowmereCounseling.example

Font styles to use
Serif

Requirements
Must have
• Logo on Front (Large) prefer gold/silver foil on a matte dark color (i.e. black, navy, etc.); Back of Card: All other relevant information

```html
<!DOCTYPE html>
<html lang="en">
<head>
<meta charset="UTF-8">
<title>Willowmere Counseling – Business Card</title>
<link href="https://fonts.googleapis.com/css2?family=Cinzel:wght@400;600&display=swap" rel="stylesheet">
<style>
  :root {
    --backdrop: #5f5f5f;
    --card-dark: #151515;
    --card-light: #ffffff;
    --gold: #c1942f;
    --gold-deep: #a97d1e;
    --silver: #c9c9c9;
    --ink: #1c1d2b;
    --map-tone: #e9ecef;
  }
  * { box-sizing: border-box; margin: 0; padding: 0; }
  html, body {
    width: 1200px; height: 1000px; overflow: hidden;
    background: var(--backdrop);
    font-family: "Cinzel", "Times New Roman", serif;
  }
  .stage {
    position: relative; width: 1200px; height: 1000px;
    display: flex; justify-content: center; align-items: center; gap: 60px;
  }
  .card {
    width: 420px; height: 700px; position: relative;
    box-shadow: 0 18px 40px rgba(0,0,0,0.35);
  }

  /* Front */
  .card-front { background: var(--card-dark); }
  .brand {
    position: absolute; top: 230px; left: 0; right: 0;
    display: flex; flex-direction: column; align-items: center;
  }
  .brand-dot {
    width: 64px; height: 64px; border-radius: 50%;
    background: var(--gold); margin-bottom: 22px;
  }
  .brand-name {
    color: var(--gold); font-weight: 600; font-size: 34px;
    letter-spacing: 2px; text-align: center; line-height: 1.15;
    text-transform: uppercase;
  }
  .brand-rule {
    width: 300px; height: 2px; background: var(--silver); margin-top: 18px;
  }
  .tagline-band {
    position: absolute; left: 0; right: 0; top: 548px; height: 46px;
    background: var(--gold);
    display: flex; align-items: center; justify-content: center;
    color: var(--card-dark); font-size: 19px; letter-spacing: 1.5px;
    text-transform: uppercase;
  }

  /* Back */
  .card-back {
    background: var(--card-light);
    display: flex; flex-direction: column; align-items: center;
    padding-top: 62px; color: var(--ink);
  }
  .address {
    font-size: 15px; letter-spacing: 1px; text-align: center;
    text-transform: uppercase; line-height: 1.35;
  }
  .map-area {
    width: 340px; height: 190px; margin-top: 20px;
    border: 2px solid var(--gold);
    background: linear-gradient(135deg, #eef0f2, var(--map-tone) 60%, #f3ecd9);
  }
  .practice-name {
    margin-top: 36px; font-size: 25px; font-weight: 600; letter-spacing: 1px;
    text-transform: uppercase;
  }
  .role {
    margin-top: 6px; font-size: 14px; color: var(--gold); letter-spacing: 1px;
    text-transform: uppercase;
  }
  .icon-row {
    position: relative; margin-top: 22px; width: 200px; height: 28px;
    display: flex; justify-content: center; gap: 16px; align-items: center;
  }
  .icon-row::before {
    content: ""; position: absolute; left: 0; right: 0; top: 50%;
    height: 1px; background: var(--gold);
  }
  .icon {
    position: relative; width: 26px; height: 26px; border-radius: 50%;
    background: var(--gold-deep); display: flex; align-items: center; justify-content: center;
  }
  .contact-list {
    list-style: none; margin-top: 34px; text-align: center;
    font-size: 14px; letter-spacing: 0.5px; line-height: 1.75;
  }
  .contact-list .upper { text-transform: uppercase; }
</style>
</head>
<body>
<main class="stage">
  <section class="card card-front">
    <div class="brand">
      <div class="brand-dot"></div>
      <div class="brand-name">Willowmere<br>Counseling</div>
      <div class="brand-rule"></div>
    </div>
    <div class="tagline-band">Endure - Mend - Flourish</div>
  </section>

  <section class="card card-back">
    <p class="address">3870 N. Garrick Ave., Suite 214,<br>Fort Worth, TX 76132</p>
    <div class="map-area" role="img" aria-label="Street map marking the office location"></div>
    <h1 class="practice-name">Willowmere Counseling</h1>
    <p class="role">CEO - Founder</p>
    <div class="icon-row">
      <span class="icon">
        <svg width="14" height="14" viewBox="0 0 24 24" aria-hidden="true"><path fill="#151515" d="M6.6 10.8a15.2 15.2 0 0 0 6.6 6.6l2.2-2.2a1 1 0 0 1 1-.25 11.4 11.4 0 0 0 3.6.57 1 1 0 0 1 1 1V20a1 1 0 0 1-1 1A17 17 0 0 1 3 4a1 1 0 0 1 1-1h3.5a1 1 0 0 1 1 1c0 1.25.2 2.45.57 3.6a1 1 0 0 1-.25 1z"/></svg>
      </span>
      <span class="icon">
        <svg width="14" height="14" viewBox="0 0 24 24" aria-hidden="true"><rect x="3" y="6" width="18" height="12" rx="1" fill="none" stroke="#151515" stroke-width="2"/><path d="M3 7l9 6 9-6" fill="none" stroke="#151515" stroke-width="2"/></svg>
      </span>
      <span class="icon">
        <svg width="14" height="14" viewBox="0 0 24 24" aria-hidden="true"><circle cx="12" cy="12" r="9" fill="none" stroke="#151515" stroke-width="2"/><ellipse cx="12" cy="12" rx="4" ry="9" fill="none" stroke="#151515" stroke-width="2"/><path d="M3 12h18" stroke="#151515" stroke-width="2"/></svg>
      </span>
    </div>
    <ul class="contact-list">
      <li>(214) 555-0187</li>
      <li class="upper">info@willowmerecounseling.example</li>
      <li class="upper">www.WillowmereCounseling.example</li>
    </ul>
  </section>
</main>
</body>
</html>
```